Wavelume artwork for new single release

I need Wavelume artwork creating to release a new single on there.

The specs are:

Ideal size: 3000 x 3000 pixels
Minimum size: 1400 x 1400 pixels
Aspect ratio: 1:1 (must be a perfect square)
File format: JPG or PNG
Color space: sRGB
File size: Max 4MB

The song is called "Still, Can We Wander?"
The artist is "Milo Fenwright"

We have no images of Milo, so it really is open to imagination.

Target Market(s)

Wavelume listeners

Industry/Entity Type

Music

```html
<!DOCTYPE html>
<html lang="en">
<head>
<meta charset="utf-8">
<title>Still, Can We Wander? — Milo Fenwright</title>
<link href="https://fonts.googleapis.com/css2?family=Yellowtail&family=DM+Sans:wght@600&display=swap" rel="stylesheet">
<style>
  :root {
    --sky-top: #1f3f4a;
    --sky-low: #3a4a5c;
    --treeline: #1a1420;
    --field-deep: #3a1414;
    --field-red: #7a2418;
    --ember: #e0762a;
    --glow: #ffb347;
    --type: #ffffff;
    --type-shadow: #1c1f3a;
  }
  html, body {
    margin: 0;
    padding: 0;
    width: 1200px;
    height: 1200px;
    overflow: hidden;
    background: #000;
  }
  .cover {
    position: relative;
    width: 1200px;
    height: 1200px;
    overflow: hidden;
  }
  .cover__scene {
    position: absolute;
    inset: 0;
    background:
      radial-gradient(ellipse 360px 260px at 560px 1200px, var(--glow) 0%, rgba(224,118,42,0.55) 40%, rgba(224,118,42,0) 100%),
      radial-gradient(ellipse 700px 500px at 600px 700px, rgba(224,118,42,0.35) 0%, rgba(224,118,42,0) 100%),
      linear-gradient(180deg,
        var(--sky-top) 0%,
        var(--sky-low) 12%,
        var(--treeline) 16%,
        var(--treeline) 30%,
        var(--field-red) 42%,
        var(--field-deep) 62%,
        #2a0e0c 80%,
        var(--field-red) 100%);
  }
  .cover__title {
    position: absolute;
    left: 0;
    right: 0;
    top: 170px;
    margin: 0;
    text-align: center;
    font-family: "Yellowtail", cursive;
    font-weight: 400;
    color: var(--type);
    text-shadow: 6px 6px 0 var(--type-shadow);
    line-height: 0.9;
    transform: rotate(-4deg);
  }
  .cover__title-line { display: block; }
  .cover__title-line--lead { font-size: 130px; margin-left: -40px; }
  .cover__title-line--main { font-size: 230px; }
  .cover__title-line--last { font-size: 230px; margin-left: 40px; }
  .cover__artist {
    position: absolute;
    left: 0;
    right: 0;
    top: 1078px;
    margin: 0;
    text-align: center;
    font-family: "DM Sans", sans-serif;
    font-weight: 600;
    font-size: 50px;
    letter-spacing: 0.5px;
    color: var(--type);
  }
</style>
</head>
<body>
  <main class="cover">
    <div class="cover__scene" role="img" aria-label="Photograph of a figure walking through a dusky field at sunset, with glowing embers and sparks rising from a fire in the foreground"></div>
    <h1 class="cover__title">
      <span class="cover__title-line cover__title-line--lead">Still,</span>
      <span class="cover__title-line cover__title-line--main">Can We</span>
      <span class="cover__title-line cover__title-line--last">Wander?</span>
    </h1>
    <p class="cover__artist">Milo Fenwright</p>
  </main>
</body>
</html>
```